Personal Finance Author needs a postcard

Hi there,

I am a Canadian personal finance author and have published a new book called The Wealth Compass.

I teach Millennials how to create a 6-figure portfolio through investing (https://www.dariafelt.com/)

I'm speaking at some conferences so we were going to print some postcards to hand out to attendees with our info and calls-to-action on them.

I am looking for 4x6 (horizontal) postcard (no space needed for shipping label).

Logos, Headshots and Book Cover:
https://files.cloudvaultex.com/folders/8kQpZrT2mWvN4xLbJ7sHdYc3FgA9eUoRi?usp=sharing

Both sides will be full colour. I would like a clean and simple look. Our main sites are www.DariaFelt.com and www.TheWealthCompassBook.com if you want to get a sense of style and design.
I also uploaded a few marketing materials so you can see the existing designs.

Side 1:
Get Instant Access to your Free Resources - main headline

(small bullets underneath)
- The Wealth Compass Checklist
- Financial Worksheets
- Database of Investment Tools

DariaFelt.com/Resources

At the bottom, include "Don't forget to follow Daria Felt on social media:
Linkedin: @dariafelt7
Facebook: @thewealthcompassbook Instagram: @thewealthcompassbook Twitter: @WealthCompassBk"

Side 2:
Headline - Want to work directly with Daria and The Wealth Compass team to help you make your money grow and stay safe?

Work with us to (bullet point list)...
- Hire Daria as a Keynote Speaker
- Teach Financial Literacy Workshops
- Receive Financial Coaching

Want To Learn More About How We Can Help?
DariaFelt.com/Services

Include my contact info:
Daria Felt
Author | Speaker | Investor
daria@thewealthcompassbook.com
416-555-0187

Target Market(s)

Millennials who want to learn how to save and invest their money. I focus on stock market investing, real estate investing and entrepreneurship.

Industry/Entity Type

Financial Service

Font styles to use
Sans Serif

Colors

Designer to choose colors to be used in the design.

Requirements
Must have
• Photo of Daria Felt
• The Wealth Compass logo
• Green, Gold/Yellow to match existing colours
• modern business style postcard

```html
<!DOCTYPE html>
<html lang="en">
<head>
<meta charset="utf-8">
<title>The Wealth Compass – Postcard</title>
<link href="https://fonts.googleapis.com/css2?family=Barlow+Semi+Condensed:ital,wght@0,600;1,500;1,600&family=Questrial&display=swap" rel="stylesheet">
<style>
  :root {
    --green: #1b730f;
    --gold: #f0b928;
    --paper: #f2f2f2;
    --stage: #3b3b3d;
    --white: #ffffff;
    --photo-a: #c9c4bf;
    --photo-b: #8d9690;
  }
  * { box-sizing: border-box; margin: 0; padding: 0; }
  html, body { width: 1200px; height: 1200px; overflow: hidden; }
  body { background: var(--stage); position: relative; font-family: "Questrial", sans-serif; }

  .postcard {
    position: absolute; left: 237px; width: 727px; height: 484px;
    background: var(--paper); overflow: hidden;
    box-shadow: 0 6px 18px rgba(0,0,0,.35);
  }
  .postcard--front { top: 86px; }
  .postcard--back { top: 630px; }

  .headline {
    font-family: "Barlow Semi Condensed", sans-serif; font-style: italic; font-weight: 500;
    color: var(--green); position: absolute;
  }
  .accent { color: var(--gold); }

  .tick-list { position: absolute; list-style: none; color: var(--green); font-size: 14px; letter-spacing: .2px; }
  .tick-list li { display: flex; align-items: center; gap: 11px; height: 16.5px; }
  .tick-list svg { width: 13px; height: 13px; flex: none; }

  .url-pill {
    position: absolute; background: var(--green); color: var(--white);
    border-radius: 14px; display: flex; align-items: center; justify-content: center;
  }

  .band-gold { position: absolute; left: 0; height: 17px; background: var(--gold); }
  .band-green { position: absolute; left: 0; width: 100%; bottom: 0; background: var(--green); }

  /* front */
  .brand-mark {
    position: absolute; left: 130px; top: 28px; width: 205px; text-align: center;
    font-family: "Barlow Semi Condensed", sans-serif; font-weight: 600; color: var(--green);
    font-size: 40px; line-height: 34px; text-transform: uppercase;
  }
  .brand-mark small { display: block; font-size: 17px; line-height: 20px; }
  .front-headline { left: 55px; top: 157px; font-size: 22px; line-height: 25px; text-transform: uppercase; }
  .front-ticks { left: 55px; top: 242px; }
  .front-pill { left: 55px; top: 296px; width: 212px; height: 25px; font-size: 15px; }
  .social-title {
    position: absolute; left: 54px; top: 366px; color: var(--gold);
    font-family: "Barlow Semi Condensed", sans-serif; font-style: italic; font-weight: 500; font-size: 15px;
  }
  .social-list { position: absolute; left: 54px; top: 391px; list-style: none; color: var(--white); font-size: 11.5px; }
  .social-list li { display: flex; align-items: center; gap: 5px; height: 19.7px; }
  .social-dot { width: 14px; height: 14px; border-radius: 50%; background: #6fa8dc; flex: none; }
  .headshot {
    position: absolute; left: 400px; top: 12px; width: 327px; height: 472px;
    border-radius: 150px 150px 0 0;
    background: linear-gradient(180deg, #d8b59a 0%, var(--photo-a) 45%, var(--photo-b) 100%);
  }
  .name-tag {
    position: absolute; left: 584px; top: 441px; width: 88px; height: 22px; border-radius: 11px;
    background: rgba(60,90,60,.55); color: var(--paper); font-size: 11px;
    display: flex; align-items: center; justify-content: center; letter-spacing: .5px;
  }

  /* back */
  .back-headline { left: 48px; top: 60px; width: 400px; font-size: 20px; line-height: 23px; font-weight: 600; }
  .work-title { left: 48px; top: 158px; font-size: 18px; }
  .back-ticks { left: 47px; top: 182px; }
  .help-box { position: absolute; left: 47px; top: 256px; width: 306px; height: 60px; border: 2px solid var(--gold); }
  .help-box p {
    position: absolute; left: 0; right: 0; top: 8px; text-align: center; color: var(--green);
    font-family: "Barlow Semi Condensed", sans-serif; font-style: italic; font-weight: 500; font-size: 13px;
  }
  .back-pill { left: 70px; top: 27px; width: 163px; height: 19px; font-size: 12px; }
  .contact-title {
    position: absolute; left: 47px; top: 356px; color: var(--gold);
    font-family: "Barlow Semi Condensed", sans-serif; font-style: italic; font-weight: 600; font-size: 21px;
  }
  .contact-lines { position: absolute; left: 47px; top: 382px; color: var(--white); font-size: 16px; line-height: 20px; }
  .book-stack {
    position: absolute; left: 480px; top: 22px; width: 240px; height: 448px; border-radius: 6px;
    background: linear-gradient(160deg, #fafafa 0%, #e6e6e0 45%, #cfd6c8 75%, var(--green) 100%);
  }
</style>
</head>
<body>

<section class="postcard postcard--front">
  <div class="brand-mark"><small>The</small>Wealth<br>Compass</div>
  <h1 class="headline front-headline">Get instant access to your<br>free resources</h1>
  <ul class="tick-list front-ticks">
    <li><svg viewBox="0 0 14 14"><circle cx="7" cy="7" r="7" fill="#1b730f"/><path d="M3.8 7.2l2.2 2.1 4.2-4.4" fill="none" stroke="#fff" stroke-width="1.6"/></svg>The Wealth Compass Checklist</li>
    <li><svg viewBox="0 0 14 14"><circle cx="7" cy="7" r="7" fill="#1b730f"/><path d="M3.8 7.2l2.2 2.1 4.2-4.4" fill="none" stroke="#fff" stroke-width="1.6"/></svg>Financial Worksheets</li>
    <li><svg viewBox="0 0 14 14"><circle cx="7" cy="7" r="7" fill="#1b730f"/><path d="M3.8 7.2l2.2 2.1 4.2-4.4" fill="none" stroke="#fff" stroke-width="1.6"/></svg>Database of Investment Tools</li>
  </ul>
  <div class="url-pill front-pill">DariaFelt.com/Resources</div>

  <div class="band-gold" style="top:329px;width:440px"></div>
  <div class="band-green" style="height:138px"></div>
  <p class="social-title">Don’t forget to follow Daria Felt on social media</p>
  <ul class="social-list">
    <li><span class="social-dot"></span>@thewealthcompassbook</li>
    <li><span class="social-dot"></span>@dariafelt7</li>
    <li><span class="social-dot"></span>@thewealthcompassbook</li>
    <li><span class="social-dot"></span>@WealthCompassBk</li>
  </ul>

  <div class="headshot" role="img" aria-label="Portrait photo of Daria Felt in a grey blazer"></div>
  <div class="name-tag">DARIA FELT</div>
</section>

<section class="postcard postcard--back">
  <h2 class="headline back-headline">Want to work directly with Daria and The Wealth Compass team to help you make your <span class="accent">MONEY GROW</span> and <span class="accent">STAY SAFE</span>?</h2>
  <h3 class="headline work-title">Work with us to:</h3>
  <ul class="tick-list back-ticks">
    <li><svg viewBox="0 0 14 14"><circle cx="7" cy="7" r="7" fill="#1b730f"/><path d="M3.8 7.2l2.2 2.1 4.2-4.4" fill="none" stroke="#fff" stroke-width="1.6"/></svg>Hire Daria as a Keynote Speaker</li>
    <li><svg viewBox="0 0 14 14"><circle cx="7" cy="7" r="7" fill="#1b730f"/><path d="M3.8 7.2l2.2 2.1 4.2-4.4" fill="none" stroke="#fff" stroke-width="1.6"/></svg>Teach Financial Literacy Workshops</li>
    <li><svg viewBox="0 0 14 14"><circle cx="7" cy="7" r="7" fill="#1b730f"/><path d="M3.8 7.2l2.2 2.1 4.2-4.4" fill="none" stroke="#fff" stroke-width="1.6"/></svg>Receive Financial Coaching</li>
  </ul>
  <div class="help-box">
    <p>Want To Learn More About How We Can Help?</p>
    <div class="url-pill back-pill">DariaFelt.com/Services</div>
  </div>

  <div class="band-gold" style="top:330px;width:100%"></div>
  <div class="band-green" style="height:137px"></div>
  <p class="contact-title">Contact information:</p>
  <div class="contact-lines">
    Daria Felt<br>Author | Speaker | Investor<br>daria@thewealthcompassbook.com<br>416-555-0187
  </div>

  <div class="book-stack" role="img" aria-label="Stack of The Wealth Compass books with cover artwork"></div>
</section>

</body>
</html>
```